Wedding Decor and Entertianment business card

Company - We run a weddings and events company called Amber Finch, we provide most entertainment and decor services to our customers.

Initial idea is ....
A simple business card with logo on the front, this will be spot varnish. On a matt black background.
The reverse will be simple contact information.

But happy to try things outside of the box and would welcome some crazy ideas.

Target Market(s)

wedding couples - 21 - 40
High end wedding venues.

Industry/Entity Type

Wedding

Contact Information for Business Card

01492 718 263
amberfinchevents.co.uk
rowan@amberfinchevents.co.uk
or
helena@amberfinchevents.co.uk

Requirements
Nice to have
• black matt background with spot varnish logo on the front.

```html
<!DOCTYPE html>
<html lang="en">
<head>
<meta charset="utf-8">
<title>Amber Finch – Contact Card</title>
<link rel="stylesheet" href="https://fonts.googleapis.com/css2?family=Fondamento:ital@1&display=swap">
<style>
  :root {
    --card-black: #060606;
    --ink-light: #f2f2f2;
    --lace-grey: #3a3a3a;
  }
  html, body {
    margin: 0;
    padding: 0;
    width: 1200px;
    height: 686px;
    overflow: hidden;
    background: var(--card-black);
  }
  .card {
    position: relative;
    width: 1200px;
    height: 686px;
    background: var(--card-black);
    overflow: hidden;
  }
  .lace {
    position: absolute;
  }
  .lace--top-left {
    left: 0;
    top: 0;
    width: 290px;
    height: 300px;
    background: radial-gradient(ellipse at 20% 15%, var(--lace-grey) 0%, rgba(58,58,58,0.55) 40%, rgba(6,6,6,0) 72%);
  }
  .lace--bottom-right {
    right: 0;
    bottom: 0;
    width: 420px;
    height: 170px;
    background: radial-gradient(ellipse at 85% 90%, var(--lace-grey) 0%, rgba(58,58,58,0.5) 40%, rgba(6,6,6,0) 72%);
  }
  .contact {
    position: absolute;
    left: 0;
    right: 0;
    top: 205px;
    margin: 0;
    padding: 0;
    list-style: none;
    text-align: center;
    font-family: "Fondamento", "Georgia", serif;
    font-style: italic;
    font-size: 50px;
    line-height: 106px;
    color: var(--ink-light);
    letter-spacing: 1px;
  }
  .contact__item {
    margin: 0;
  }
</style>
</head>
<body>
  <main class="card">
    <div class="lace lace--top-left" role="img" aria-label="Grey lace floral ornament in the top left corner"></div>
    <div class="lace lace--bottom-right" role="img" aria-label="Grey lace paisley ornament in the bottom right corner"></div>
    <ul class="contact">
      <li class="contact__item contact__phone">01492 718 263</li>
      <li class="contact__item contact__web">amberfinchevents.co.uk</li>
      <li class="contact__item contact__email">rowan@amberfinchevents.co.uk</li>
    </ul>
  </main>
</body>
</html>
```